Maple Lantern Kids - pictora Photospot

We are looking for an pictora type wal for our pediatric dental office. We are thinking it could be weaved into a whole bunch of what we do (i.e. potentially water marked or faded in the background on letterhead, as an pictroa type wall in the practice, as a banner or section of the home page on the website, on rack cards, etc.) I’m thinking it would utilize a nice fun cursive script for the wording "Maple Lantern Kids is the spot for...." and a bunch of different sized “spots” with meaningful words that speak to who we are. That list would include things like:

• Fun
• Smiles
• Laughter
• Caring
• Comfort
• Amazing
• Kids
• Toddlers
• Teens
• Friends
• Family
• Health
• Education
• Cheer
• Positivity
• Exceptional Care

From a color perspective….we could look at a couple of options. We could have one version that has it washed out and in the background (more subliminal). We could have one version that was consistent with the colors in our logo. And we could have one version that popped with more color by utilizing the colors in some of the artwork we use throughout the office (snowboard picture as an example)

Target Market(s)

Appeal to hip families with kids

Industry/Entity Type

Pediatric Dental

Font styles to use
Other font styles liked:
• something modern, hip, playful and fun

Colors
0054AA
0677BA
7BADD7
CADEEF
E8F1F8
0094D4
00A9DD
6FCCEA
C7EBF8
E9F6FB
00AB8E
00BBA5
67D7C9
C6EFE9
E9F9F6

Requirements
Must have
• Use of existing logo and a play on "spots" or polka dots with symbpolic wording. Must appeal to young parents and kiddos (including hip teens)
Should not have
• SHOULDNT BE OVER THE TOP KIDS.

```html
<!DOCTYPE html>
<html lang="en">
<head>
<meta charset="utf-8">
<title>Maple Lantern Kids is the spot for....</title>
<link href="https://fonts.googleapis.com/css2?family=Leckerli+One&family=Amatic+SC:wght@400;700&family=Fredoka:wght@500;600&display=swap" rel="stylesheet">
<style>
  :root {
    --navy: #1a3a4d;
    --white: #ffffff;
    --bg-center: #ffffff;
    --bg-edge: #f1f2f2;
    --blue-deep: #1456aa;
    --blue: #1a94d4;
    --blue-bright: #00a9dd;
    --blue-sky: #6fcbea;
    --blue-pale: #c7ebf8;
    --blue-soft: #7bacd7;
    --teal: #15ab8e;
    --teal-soft: #7dcdc5;
  }
  html, body { margin: 0; padding: 0; overflow: hidden; }
  .canvas {
    position: relative;
    width: 1051px;
    height: 1200px;
    overflow: hidden;
    background: radial-gradient(circle at 50% 55%, var(--bg-center) 0%, var(--bg-edge) 100%);
  }
  .arch-art {
    position: absolute;
    left: 484px;
    top: 132px;
    width: 224px;
    height: 126px;
    border-radius: 22px 22px 0 0;
    background: linear-gradient(180deg, #bfe3f3 0%, #d3efec 55%, #e4f4fa 100%);
  }
  .sparkle-art {
    position: absolute;
    border-radius: 50%;
    background: var(--blue-pale);
  }
  .headline-art { position: absolute; left: 0; top: 0; }
  .headline-text, .headline-shadow {
    font-family: "Leckerli One", cursive;
    font-size: 84px;
    stroke: var(--navy);
    stroke-width: 14px;
    stroke-linejoin: round;
  }
  .headline-text { fill: var(--white); paint-order: stroke; }
  .headline-shadow { fill: var(--navy); }
  .spot {
    position: absolute;
    width: 84px;
    height: 84px;
    margin: -42px 0 0 -42px;
    border-radius: 50%;
    background: var(--navy);
    color: var(--white);
    display: flex;
    align-items: center;
    justify-content: center;
    text-align: center;
    line-height: 1;
  }
  .spot--round { font-family: "Fredoka", sans-serif; font-weight: 500; font-size: 26px; }
  .spot--caps { font-family: "Fredoka", sans-serif; font-weight: 600; font-size: 20px; text-transform: uppercase; }
  .spot--bold { font-family: "Amatic SC", sans-serif; font-weight: 700; font-size: 30px; }
  .spot--thin { font-family: "Amatic SC", sans-serif; font-weight: 400; font-size: 27px; }
  .spot--small { font-size: 22px; line-height: 0.95; }
  .dot {
    position: absolute;
    width: 28px;
    height: 28px;
    margin: -14px 0 0 -14px;
    border-radius: 50%;
  }
  .hub {
    position: absolute;
    left: 513px;
    top: 768px;
    width: 176px;
    height: 176px;
    margin: -88px 0 0 -88px;
    border-radius: 50%;
    background: var(--navy);
  }
  .hub-art {
    position: absolute;
    left: 22px;
    top: 46px;
    width: 128px;
    height: 64px;
    border-radius: 24px 30px 12px 12px;
    background: linear-gradient(135deg, #e9f6fb 0%, #a9d6ee 60%, #7bb7dc 100%);
  }
  .hub-place {
    position: absolute;
    left: 0;
    right: 0;
    top: 114px;
    text-align: center;
    font-family: "Fredoka", sans-serif;
    font-weight: 600;
    font-size: 12.5px;
    letter-spacing: 0.5px;
    color: var(--white);
  }
</style>
</head>
<body>
<div class="canvas">
  <div class="arch-art" role="img" aria-label="Decorative three-band arch in blue, teal and pale blue"></div>
  <div class="sparkle-art" style="left:708px;top:138px;width:28px;height:28px;background:#a6ddd6" role="img" aria-label="Small teal sparkle decoration"></div>
  <div class="sparkle-art" style="left:445px;top:213px;width:14px;height:14px;background:#7fd0ee" role="img" aria-label="Small blue sparkle decoration"></div>

  <svg class="headline-art" width="1051" height="460" viewBox="0 0 1051 460">
    <g class="headline">
      <text class="headline-shadow" x="529" y="312" text-anchor="middle" textLength="840" lengthAdjust="spacingAndGlyphs">Maple Lantern Kids is</text>
      <text class="headline-text" x="525" y="304" text-anchor="middle" textLength="840" lengthAdjust="spacingAndGlyphs">Maple Lantern Kids is</text>
      <text class="headline-shadow" x="529" y="412" text-anchor="middle" textLength="550" lengthAdjust="spacingAndGlyphs">the spot for....</text>
      <text class="headline-text" x="525" y="404" text-anchor="middle" textLength="550" lengthAdjust="spacingAndGlyphs">the spot for....</text>
    </g>
  </svg>

  <div class="dot" style="left:190px;top:538px;background:var(--teal)"></div>
  <div class="dot" style="left:496px;top:497px;background:var(--blue-pale)"></div>
  <div class="dot" style="left:720px;top:549px;background:var(--teal)"></div>
  <div class="dot" style="left:534px;top:649px;background:var(--blue)"></div>
  <div class="dot" style="left:888px;top:668px;background:var(--blue-deep)"></div>
  <div class="dot" style="left:245px;top:748px;background:var(--blue-bright)"></div>
  <div class="dot" style="left:385px;top:769px;background:var(--blue-pale)"></div>
  <div class="dot" style="left:669px;top:781px;background:var(--teal-soft)"></div>
  <div class="dot" style="left:142px;top:819px;background:var(--teal-soft)"></div>
  <div class="dot" style="left:775px;top:882px;background:var(--blue-sky)"></div>
  <div class="dot" style="left:279px;top:928px;background:var(--blue-soft)"></div>
  <div class="dot" style="left:556px;top:923px;background:var(--teal)"></div>
  <div class="dot" style="left:181px;top:1035px;background:var(--blue-pale)"></div>
  <div class="dot" style="left:451px;top:1048px;background:var(--teal-soft)"></div>
  <div class="dot" style="left:704px;top:1022px;background:var(--blue-pale)"></div>

  <div class="spot spot--round" style="left:310px;top:548px">Fun</div>
  <div class="spot spot--caps" style="left:443px;top:578px">Smiles</div>
  <div class="spot spot--thin spot--small" style="left:598px;top:548px">Exceptional<br>Care</div>
  <div class="spot spot--bold" style="left:822px;top:563px">CHEER</div>
  <div class="spot spot--thin" style="left:170px;top:666px">EDUCATION</div>
  <div class="spot spot--thin" style="left:330px;top:683px">COMFORT</div>
  <div class="spot spot--thin" style="left:659px;top:651px">CARING</div>
  <div class="spot spot--bold" style="left:782px;top:721px">TEENS</div>
  <div class="spot spot--caps" style="left:310px;top:830px;font-size:26px">Kids</div>
  <div class="spot spot--thin" style="left:888px;top:833px">LAUGHTER</div>
  <div class="spot spot--thin" style="left:171px;top:921px">AMAZING</div>
  <div class="spot spot--thin" style="left:445px;top:929px">TODDLERS</div>
  <div class="spot spot--bold" style="left:669px;top:893px">HEALTH</div>
  <div class="spot spot--thin spot--small" style="left:847px;top:991px">POSITIVITY</div>
  <div class="spot spot--bold" style="left:320px;top:1024px">FRIENDS</div>
  <div class="spot spot--bold" style="left:581px;top:1022px">FAMILY</div>

  <div class="hub">
    <div class="hub-art" role="img" aria-label="Soft watercolor-blue illustration of a walking bear"></div>
    <div class="hub-place">ELM RIDGE, CA</div>
  </div>
</div>
</body>
</html>
```